We want a business card/punch card for our business. We are including examples of our current business card (we like the front of our business card and not looking to remake it). We need only back side to be designed in form of a punch card (we are including a sample of the punch card we made, but are unsatisfied). For each $180 spend (9 punches) our clients have $20 off.

Colors
886aae

```html
<!DOCTYPE html>
<html lang="en">
<head>
<meta charset="utf-8">
<title>Lumen Practices – Business Card and Punch Card</title>
<link rel="stylesheet" href="https://fonts.googleapis.com/css2?family=Crimson+Text:wght@400&family=Lato:wght@400;700&display=swap">
<style>
  :root {
    --page: #2c2c2c;
    --card: #050505;
    --brand: #5d63b8;
    --accent: #886aae;
    --ink: #f2f2f2;
    --punch: #5a62b6;
    --punch-ring: #d9d2b6;
  }
  * { margin: 0; padding: 0; box-sizing: border-box; }
  html, body { width: 1200px; height: 1200px; overflow: hidden; background: var(--page); }
  .card {
    position: absolute; left: 223px; width: 815px; height: 464px;
    background: var(--card); overflow: hidden;
  }
  .card--front { top: 77px; }
  .card--back { top: 658px; }

  /* Front */
  .front-brand {
    position: absolute; left: 40px; top: 232px; width: 320px;
    display: flex; align-items: center; justify-content: center; gap: 12px;
    font-family: "Crimson Text", serif; font-size: 40px; line-height: 48px; color: var(--brand);
    white-space: nowrap;
  }
  .front-brand__dot { width: 16px; height: 16px; border-radius: 50%; background: var(--brand); flex: none; }
  .contact { position: absolute; left: 440px; top: 254px; font-family: "Crimson Text", serif; }
  .contact__name { font-size: 30px; color: var(--brand); letter-spacing: 0.5px; line-height: 38px; margin-bottom: 2px; }
  .contact__row { display: flex; align-items: center; height: 26px; font-size: 20px; color: var(--ink); white-space: nowrap; }
  .contact__icon { width: 16px; height: 16px; margin: 0 14px 0 0; flex: none; }

  /* Back (content set on its side) */
  .back-frame {
    position: absolute; left: 0; top: 0; width: 464px; height: 815px;
    transform-origin: 0 0; transform: translate(815px, 0) rotate(90deg);
  }
  .back-brand {
    position: absolute; left: 20px; top: 44px; width: 424px; text-align: center;
    font-family: "Crimson Text", serif; font-size: 60px; line-height: 64px; color: var(--brand);
  }
  .services { position: absolute; left: 0; top: 280px; width: 464px; font-family: "Lato", sans-serif; color: var(--ink); font-size: 17px; text-align: center; }
  .services__line { height: 28px; line-height: 28px; white-space: nowrap; }
  .services__sep { display: inline-block; width: 9px; height: 9px; border-radius: 50%; background: var(--brand); margin: 0 5px; vertical-align: 1px; }
  .services__rule { height: 2px; background: var(--brand); margin: 0 auto; }
  .services__rule--long { width: 428px; }
  .services__rule--short { width: 196px; }

  .punches {
    position: absolute; left: 40px; top: 455px;
    display: grid; grid-template-columns: repeat(3, 108px); grid-auto-rows: 108px; gap: 8px 26px;
  }
  .punch { position: relative; width: 108px; height: 108px; }
  .punch__seal { position: absolute; inset: 0; }
  .punch__value {
    position: absolute; inset: 0; display: flex; align-items: center; justify-content: center;
    font-family: "Lato", sans-serif; font-weight: 700; font-size: 22px; color: #ffffff;
  }
</style>
</head>
<body>

<section class="card card--front" aria-label="Business card front">
  <div class="front-brand"><span class="front-brand__dot"></span>Lumen Practices</div>

  <div class="contact">
    <div class="contact__name">SELENE VARGA</div>
    <div class="contact__row">
      <svg class="contact__icon" viewBox="0 0 16 16" aria-hidden="true"><path d="M4 1.5l2.3 3-1.4 1.6c.8 1.9 2.2 3.3 4 4.1l1.6-1.4 3 2.3-1.3 2.6C6.6 13.5 2.3 9.2 1.4 3z" fill="var(--brand)"/></svg>
      +(425) -555- 0142
    </div>
    <div class="contact__row">
      <svg class="contact__icon" viewBox="0 0 16 16" aria-hidden="true"><rect x="1" y="3" width="14" height="10" fill="var(--brand)"/><path d="M1.5 3.5L8 9l6.5-5.5" stroke="var(--card)" stroke-width="1.2" fill="none"/></svg>
      hello@lumenpractices.com
    </div>
    <div class="contact__row">
      <svg class="contact__icon" viewBox="0 0 16 16" aria-hidden="true"><circle cx="8" cy="8" r="6.5" stroke="var(--brand)" stroke-width="1.3" fill="none"/><ellipse cx="8" cy="8" rx="2.8" ry="6.5" stroke="var(--brand)" stroke-width="1" fill="none"/><path d="M1.5 8h13M2.5 5h11M2.5 11h11" stroke="var(--brand)" stroke-width="1"/></svg>
      www.lumenpractices.com
    </div>
    <div class="contact__row">
      <svg class="contact__icon" viewBox="0 0 16 16" aria-hidden="true"><rect x="1.5" y="1.5" width="13" height="13" rx="2" fill="var(--brand)"/></svg>
      social.example/LumenPractices
    </div>
    <div class="contact__row">
      <svg class="contact__icon" viewBox="0 0 16 16" aria-hidden="true"><circle cx="8" cy="8" r="6.5" fill="var(--brand)"/></svg>
      groups.example/Lumen-Practices
    </div>
  </div>
</section>

<section class="card card--back" aria-label="Punch card back">
  <div class="back-frame">
    <div class="back-brand">Lumen<br>Practices</div>

    <div class="services">
      <div class="services__line">Tantra<span class="services__sep"></span>Tao<span class="services__sep"></span>Yaga<span class="services__sep"></span>Tai Chi<span class="services__sep"></span>Reiki</div>
      <div class="services__rule services__rule--long"></div>
      <div class="services__line">Sacred Sexuality<span class="services__sep"></span>Sexual Healing<span class="services__sep"></span>Sound Healing</div>
      <div class="services__line">Energy Work<span class="services__sep"></span>Rituals</div>
      <div class="services__rule services__rule--short"></div>
      <div class="services__line">Partners Yoga<span class="services__sep"></span>Four Hand Massage</div>
    </div>

    <div class="punches">
      <div class="punch"><svg class="punch__seal" viewBox="0 0 108 108" role="img" aria-label="Ornamental mandala punch seal"><circle cx="54" cy="54" r="53" fill="var(--punch-ring)" opacity="0.35"/><circle cx="54" cy="54" r="42" fill="none" stroke="var(--punch-ring)" stroke-width="2"/><circle cx="54" cy="54" r="38" fill="var(--punch)"/></svg><span class="punch__value">180$</span></div>
      <div class="punch"><svg class="punch__seal" viewBox="0 0 108 108" role="img" aria-label="Ornamental mandala punch seal"><circle cx="54" cy="54" r="53" fill="var(--punch-ring)" opacity="0.35"/><circle cx="54" cy="54" r="42" fill="none" stroke="var(--punch-ring)" stroke-width="2"/><circle cx="54" cy="54" r="38" fill="var(--punch)"/></svg><span class="punch__value">180$</span></div>
      <div class="punch"><svg class="punch__seal" viewBox="0 0 108 108" role="img" aria-label="Ornamental mandala punch seal"><circle cx="54" cy="54" r="53" fill="var(--punch-ring)" opacity="0.35"/><circle cx="54" cy="54" r="42" fill="none" stroke="var(--punch-ring)" stroke-width="2"/><circle cx="54" cy="54" r="38" fill="var(--punch)"/></svg><span class="punch__value">180$</span></div>
      <div class="punch"><svg class="punch__seal" viewBox="0 0 108 108" role="img" aria-label="Ornamental mandala punch seal"><circle cx="54" cy="54" r="53" fill="var(--punch-ring)" opacity="0.35"/><circle cx="54" cy="54" r="42" fill="none" stroke="var(--punch-ring)" stroke-width="2"/><circle cx="54" cy="54" r="38" fill="var(--punch)"/></svg><span class="punch__value">180$</span></div>
      <div class="punch"><svg class="punch__seal" viewBox="0 0 108 108" role="img" aria-label="Ornamental mandala punch seal"><circle cx="54" cy="54" r="53" fill="var(--punch-ring)" opacity="0.35"/><circle cx="54" cy="54" r="42" fill="none" stroke="var(--punch-ring)" stroke-width="2"/><circle cx="54" cy="54" r="38" fill="var(--punch)"/></svg><span class="punch__value">180$</span></div>
      <div class="punch"><svg class="punch__seal" viewBox="0 0 108 108" role="img" aria-label="Ornamental mandala punch seal"><circle cx="54" cy="54" r="53" fill="var(--punch-ring)" opacity="0.35"/><circle cx="54" cy="54" r="42" fill="none" stroke="var(--punch-ring)" stroke-width="2"/><circle cx="54" cy="54" r="38" fill="var(--punch)"/></svg><span class="punch__value">180$</span></div>
      <div class="punch"><svg class="punch__seal" viewBox="0 0 108 108" role="img" aria-label="Ornamental mandala punch seal"><circle cx="54" cy="54" r="53" fill="var(--punch-ring)" opacity="0.35"/><circle cx="54" cy="54" r="42" fill="none" stroke="var(--punch-ring)" stroke-width="2"/><circle cx="54" cy="54" r="38" fill="var(--punch)"/></svg><span class="punch__value">180$</span></div>
      <div class="punch"><svg class="punch__seal" viewBox="0 0 108 108" role="img" aria-label="Ornamental mandala punch seal"><circle cx="54" cy="54" r="53" fill="var(--punch-ring)" opacity="0.35"/><circle cx="54" cy="54" r="42" fill="none" stroke="var(--punch-ring)" stroke-width="2"/><circle cx="54" cy="54" r="38" fill="var(--punch)"/></svg><span class="punch__value">180$</span></div>
      <div class="punch"><svg class="punch__seal" viewBox="0 0 108 108" role="img" aria-label="Ornamental mandala punch seal"><circle cx="54" cy="54" r="53" fill="var(--punch-ring)" opacity="0.35"/><circle cx="54" cy="54" r="42" fill="none" stroke="var(--punch-ring)" stroke-width="2"/><circle cx="54" cy="54" r="38" fill="var(--punch)"/></svg><span class="punch__value">180$</span></div>
    </div>
  </div>
</section>

</body>
</html>
```